Trading Cards

I want someone to design custom trading cards for my pro wrestling gig.

Target Market(s)

Pro wrestling fans

Requirements
Must have
• I will upload 8 photos. I need a card for each.
Nice to have
• I would like the card trimmed out on silver and feature the Iron Tide Logo I uploaded on the top center. The back of the card can be black with the same logo centered.

```html
<!DOCTYPE html>
<html lang="en">
<head>
<meta charset="utf-8">
<title>Iron Tide Wrestling – Trading Card</title>
<link rel="stylesheet" href="https://fonts.googleapis.com/css2?family=Oswald:wght@500;600;700&display=swap">
<style>
  :root {
    --bg: #d7d7e0;
    --card: #0c0c0d;
    --card-mid: #1b1b1d;
    --tab: #0a0a0b;
    --silver-hi: #f2f2f2;
    --silver-lo: #7d7d82;
    --red: #ff3419;
    --yellow: #ffdc3a;
    --rule: #6d6d70;
  }
  * { box-sizing: border-box; margin: 0; padding: 0; }
  html, body { width: 1200px; height: 1200px; overflow: hidden; background: var(--bg); }
  body { position: relative; font-family: "Oswald", sans-serif; }

  .card {
    position: absolute; top: 285px; width: 450px; height: 629px;
    background: radial-gradient(ellipse at 50% 40%, var(--card-mid), var(--card) 75%);
  }
  .card--front { left: 118px; }
  .card--back { left: 632px; }
  .card-frame, .card-tabs { position: absolute; inset: 0; width: 100%; height: 100%; }
  .card-tabs { z-index: 2; }

  .brand-mark {
    position: absolute; left: 0; right: 0; text-align: center;
    color: var(--red); font-weight: 700; text-transform: uppercase; line-height: 0.92;
    letter-spacing: 1px;
  }
  .brand-mark--front { top: 36px; font-size: 33px; }
  .brand-mark--back { top: 250px; font-size: 66px; }
  .brand-mark span { display: block; }
  .brand-mark .brand-sub { font-size: 0.72em; }

  .photo-frame {
    position: absolute; left: 55px; top: 112px; width: 340px; height: 439px; z-index: 1;
    background: linear-gradient(160deg, var(--silver-hi), var(--silver-lo) 60%, #c8c8cc);
    clip-path: polygon(13% 0, 87% 0, 100% 10%, 100% 90%, 87% 100%, 13% 100%, 0 90%, 0 10%);
  }
  .photo {
    position: absolute; left: 12px; top: 12px; right: 12px; bottom: 12px;
    background: linear-gradient(170deg, #8d86b8 0%, #5e5590 35%, #3a3140 60%, #2a2024 100%);
    clip-path: polygon(12% 0, 88% 0, 100% 8%, 100% 92%, 88% 100%, 12% 100%, 0 92%, 0 8%);
  }

  .name-tab {
    position: absolute; left: 31px; top: 334px; z-index: 3;
    transform: translate(-50%, -50%) rotate(-90deg);
    white-space: nowrap; color: var(--yellow); font-weight: 500; font-size: 17px; letter-spacing: 0.5px;
  }

  .stats {
    position: absolute; left: 358px; top: 232px; width: 92px; z-index: 3;
    text-align: center; text-transform: uppercase;
  }
  .stat-label { color: var(--red); font-weight: 500; font-size: 16px; line-height: 1.1; }
  .stat-value { color: var(--yellow); font-weight: 600; font-size: 24px; line-height: 1.15; }
  .stat-value--small { font-size: 17px; line-height: 1.25; font-weight: 500; margin-top: 4px; }
  .stat-rule { height: 1px; background: var(--rule); margin: 7px 8px 8px; }

  .division {
    position: absolute; left: 0; right: 0; top: 557px; text-align: center;
    color: var(--red); font-weight: 600; font-size: 34px; letter-spacing: 0.5px;
  }
</style>
</head>
<body>

<svg width="0" height="0" style="position:absolute">
  <defs>
    <linearGradient id="silver" x1="0" y1="0" x2="1" y2="1">
      <stop offset="0" stop-color="#f4f4f4"/>
      <stop offset="0.45" stop-color="#8a8a8f"/>
      <stop offset="0.7" stop-color="#e8e8ea"/>
      <stop offset="1" stop-color="#77777c"/>
    </linearGradient>
    <g id="frame-lines" fill="none" stroke="url(#silver)">
      <polygon points="80,8 370,8 442,75 442,554 370,621 80,621 8,554 8,75" stroke-width="4"/>
      <polygon points="92,18 358,18 432,86 432,543 358,611 92,611 18,543 18,86" stroke-width="1.5"/>
      <polyline points="6,60 6,6 60,6" stroke-width="3"/>
      <polyline points="390,6 444,6 444,60" stroke-width="3"/>
      <polyline points="6,569 6,623 60,623" stroke-width="3"/>
      <polyline points="390,623 444,623 444,569" stroke-width="3"/>
      <polygon points="20,20 40,20 20,40" stroke-width="2"/>
      <polygon points="430,20 410,20 430,40" stroke-width="2"/>
      <polygon points="20,609 40,609 20,589" stroke-width="2"/>
      <polygon points="430,609 410,609 430,589" stroke-width="2"/>
    </g>
  </defs>
</svg>

<section class="card card--front">
  <svg class="card-frame" viewBox="0 0 450 629" aria-hidden="true">
    <use href="#frame-lines"/>
  </svg>

  <div class="brand-mark brand-mark--front">
    <span>Iron Tide</span>
    <span class="brand-sub">Wrestling</span>
  </div>

  <div class="photo-frame">
    <div class="photo" role="img" aria-label="Wrestler in black and yellow singlet standing on the ring apron under the arena ceiling"></div>
  </div>

  <svg class="card-tabs" viewBox="0 0 450 629" aria-hidden="true">
    <polygon points="0,185 61,237 61,432 0,483" fill="var(--tab)" stroke="url(#silver)" stroke-width="3"/>
    <polygon points="452,181 400,181 356,224 356,440 400,483 452,483" fill="var(--tab)" stroke="url(#silver)" stroke-width="3"/>
  </svg>

  <div class="name-tab">MARCUS “THE TITAN” HALE</div>

  <div class="stats">
    <div class="stat-label">Height</div>
    <div class="stat-value">6’ 3”</div>
    <div class="stat-rule"></div>
    <div class="stat-label">Weight</div>
    <div class="stat-value">245 LBS</div>
    <div class="stat-rule"></div>
    <div class="stat-label">Hometown</div>
    <div class="stat-value stat-value--small">Nashville<br>Tennessee</div>
  </div>

  <div class="division">HEAVYWEIGHT</div>
</section>

<section class="card card--back">
  <svg class="card-frame" viewBox="0 0 450 629" aria-hidden="true">
    <use href="#frame-lines"/>
  </svg>
  <div class="brand-mark brand-mark--back">
    <span>Iron Tide</span>
    <span class="brand-sub">Wrestling</span>
  </div>
</section>

</body>
</html>
```